IT Company Business Card design

Brisk Node is a new computer solutions business focusing on setting up servers and computer systems for small to medium sized businesses.

A business client will either request a solution, or support for a current system and we will turn up on site to provide these services.

We are bast in Harbourton, Kestrel Coast.

We are looking for unique business card's that stand out and show off the business in a professional light.

Open to all idea's etc.

Industry/Entity Type

Computer

Requirements
Must have
• Business Logo (AI file attached)
Employee Name
Business title
Business landline number
Cell phone number
Email
Web URL
Nice to have
• Could be nice to have some keywords (possibly on the back) such as:

Business IT solutions
Network installations
Phone solutions
Server management
Software diagnostics

The above is not needed, just an idea.

```html
<!DOCTYPE html>
<html lang="en">
<head>
<meta charset="utf-8">
<title>Brisk Node – Business Card</title>
<link href="https://fonts.googleapis.com/css2?family=Jost:wght@400;500&display=swap" rel="stylesheet">
<style>
  :root {
    --page: #ffffff;
    --navy: #243068;
    --ocean: #0a6aa2;
    --cyan: #00a9e2;
    --card-white: #ffffff;
    --ink-navy: #0e2c68;
    --ink-dark: #1b1b1b;
    --mark-blue: #1b9ad6;
    --divider: #1d2a44;
  }
  html, body {
    margin: 0;
    padding: 0;
    width: 1200px;
    height: 805px;
    overflow: hidden;
    background: var(--page);
  }
  .canvas {
    position: relative;
    width: 1200px;
    height: 805px;
    font-family: "Jost", "Futura", sans-serif;
  }
  .card-art {
    position: absolute;
    inset: 0;
  }
  .brand-name {
    position: absolute;
    left: 850px;
    top: 120px;
    margin: 0;
    font-size: 34px;
    font-weight: 400;
    letter-spacing: 2px;
    color: var(--ink-dark);
    line-height: 1;
    white-space: nowrap;
  }
  .contact-block {
    position: absolute;
    left: 203px;
    top: 277px;
    margin: 0;
  }
  .person-name {
    margin: 0;
    font-size: 37px;
    font-weight: 500;
    color: var(--ink-navy);
    line-height: 40px;
    letter-spacing: -0.3px;
  }
  .person-role {
    margin: 0;
    font-size: 29px;
    font-weight: 400;
    color: var(--ink-navy);
    line-height: 36px;
  }
  .details {
    list-style: none;
    margin: 40px 0 0;
    padding: 0;
    font-size: 30px;
    font-weight: 400;
    color: var(--ink-dark);
    line-height: 38px;
    white-space: nowrap;
  }
</style>
</head>
<body>
<main class="canvas">
  <svg class="card-art" width="1200" height="805" viewBox="0 0 1200 805" aria-hidden="true">
    <defs>
      <linearGradient id="card-gradient" x1="120" y1="573" x2="1100" y2="41" gradientUnits="userSpaceOnUse">
        <stop offset="0" stop-color="var(--navy)"/>
        <stop offset="0.45" stop-color="var(--ocean)"/>
        <stop offset="1" stop-color="var(--cyan)"/>
      </linearGradient>
      <clipPath id="card-clip">
        <rect x="120" y="41" width="980" height="532"/>
      </clipPath>
      <filter id="panel-shadow" x="-20%" y="-20%" width="140%" height="140%">
        <feDropShadow dx="6" dy="-2" stdDeviation="14" flood-color="#001838" flood-opacity="0.65"/>
      </filter>
    </defs>
    <rect class="card-face" x="120" y="41" width="980" height="532" fill="url(#card-gradient)"/>
    <g clip-path="url(#card-clip)">
      <path class="info-panel" filter="url(#panel-shadow)" fill="var(--card-white)"
            d="M188 233 L778 298 Q800 301 797 324 L765 620 L112 620 L160 258 Q163 233 188 233 Z"/>
    </g>
    <circle class="brand-dot" cx="765" cy="137" r="52" fill="var(--mark-blue)"/>
    <line class="brand-divider" x1="834" y1="95" x2="834" y2="195" stroke="var(--divider)" stroke-width="1.5"/>
  </svg>

  <p class="brand-name">BRISK NODE</p>

  <section class="contact-block">
    <h1 class="person-name">NAME SURNAME</h1>
    <p class="person-role">POSITION</p>
    <ul class="details">
      <li>0000 STREET, Harbourton, Kestrel Coast</li>
      <li>000 000 000</li>
      <li>hello@brisknode.com</li>
      <li>www.brisknode.net</li>
    </ul>
  </section>
</main>
</body>
</html>
```